VALMIKE GROUP

This is a company that provides executive protection. Our motto is "New Era in Protection"... I don't want this to look like other security websites. I want it to be clean and sharp and represent a new era. We are based in the bay area so maybe a picture of San Francisco in the background?
I want it to be able to funnel down a couple different categories.
1. About Us
2. Services (Executive Protection, Covert Protection, Residential Protection & Intelligence)
3. Iron Finch (Training & Consulting)
4. Contact Us
I want it to be very clean and modern. I don't want there to be any pictures of bodyguards with ear pieces like every other website.
Target Market(s)
Ultra High Net Worth Individuals
Coding
Coded - Design and coding required
Number of Pages Required
1 page
Requirements
Must have
- Colors of my Symbol
Nice to have
- City in the background, San Francisco, New York or the Pinehallow Club in Montana.
Should not have
- Should not look like an KVM website or have photos of bodyguards. I want this to be a clean and simple website with my logo

```html
<!DOCTYPE html>
<html lang="en">
<head>
<meta charset="utf-8">
<title>VALMIKE GROUP — New Era in Protection</title>
<link rel="stylesheet" href="https://fonts.googleapis.com/css2?family=Orbitron:wght@700;900&family=Poppins:wght@400;500;600;700&display=swap">
<style>
:root{
  --red:#9b1b1e;
  --red-bright:#c8232a;
  --ink:#111111;
  --text:#333333;
  --grey-band:#e9e9e9;
  --field:#e6e6e6;
  --white:#ffffff;
  --footer:#111111;
  --display:'Orbitron',sans-serif;
  --body:'Poppins',sans-serif;
}
*{margin:0;padding:0;box-sizing:border-box}
html,body{width:1200px;height:3540px;overflow:hidden}
body{position:relative;background:var(--white);font-family:var(--body);color:var(--text)}
.abs{position:absolute}

/* header */
.site-header{left:0;top:0;width:1200px;height:64px;background:var(--white);z-index:5}
.brand{left:88px;top:18px;display:flex;align-items:center;gap:10px;font-family:var(--display);font-weight:700;font-size:19px;color:var(--ink);letter-spacing:1px}
.brand-mark{width:14px;height:14px;background:var(--red)}
.main-nav{right:89px;top:15px;display:flex;align-items:center;gap:25px;font-weight:600;font-size:14px;color:var(--ink)}
.main-nav .active{color:var(--red)}
.nav-cta{border:2px solid var(--red);color:var(--red);padding:6px 19px}

/* hero */
.hero{left:0;top:64px;width:1200px;height:785px}
.hero-photo{left:0;top:0;width:1200px;height:785px;background:linear-gradient(180deg,#262838 0%,#3a3a4d 40%,#4a2a25 65%,#8a3a1c 80%,#2a1a20 100%)}
.hero-title{left:0;width:1200px;text-align:center;color:var(--white);font-family:var(--display);font-weight:900}
.hero-kicker{top:338px;font-size:28px;letter-spacing:1px}
.hero-motto{top:371px;font-size:50px;letter-spacing:1px}
.hero-shape{left:0;top:0}

/* about */
.eyebrow{font-family:var(--display);font-weight:700;color:var(--red);font-size:24px;letter-spacing:1px}
.section-title{font-family:var(--display);font-weight:900;color:var(--ink);font-size:37px;letter-spacing:1px;line-height:1.1}
.copy{font-size:15px;line-height:24px;color:var(--text)}
.about-eyebrow{left:88px;top:976px}
.about-title{left:88px;top:1004px}
.about-copy{left:600px;top:968px;width:505px}
.red-rule{width:4px;background:var(--red)}

/* services */
.services-band{left:0;top:1225px;width:1200px;height:671px;background:var(--grey-band)}
.center-head{left:0;width:1200px;text-align:center}
.service-card{width:330px;height:358px;top:1433px}
.service-card svg.card-bg{position:absolute;left:0;top:0}
.service-icon{position:absolute;left:115px;top:42px}
.service-name{position:absolute;left:0;top:148px;width:100%;text-align:center;font-weight:700;font-size:17px;color:var(--ink)}
.service-copy{position:absolute;left:20px;top:178px;width:290px;text-align:center;font-size:13px;line-height:20px;color:var(--text)}
.diamond-btn{position:absolute;left:145px;top:258px;width:32px;height:32px}

/* iron finch */
.finch-eyebrow{left:89px;top:2105px}
.finch-title{left:89px;top:2133px;font-size:40px}
.finch-copy{left:89px;top:2215px;width:505px}
.read-more{left:89px;top:2375px;width:135px;height:36px;border:2px solid var(--ink);font-weight:600;font-size:15px;color:var(--ink);display:flex;align-items:center;justify-content:center}
.finch-visual{left:672px;top:2057px;width:389px;height:429px;background:linear-gradient(135deg,#a81d22,#d42a30 60%,#9b1b1e)}

/* contact */
.contact-bg{left:0;top:2600px;width:1200px;height:676px;background:linear-gradient(180deg,#ffffff 0%,#f0f0f0 45%,#d9d9d9 75%,#eeeeee 100%)}
.contact-lead{left:0;top:2723px;width:1200px;text-align:center;font-size:15px;line-height:22px;color:var(--text)}
.field{height:37px;background:var(--field);font-weight:600;font-size:13px;color:#555;padding:11px 20px}
.submit{left:533px;top:3015px;width:134px;height:35px;background:var(--red);color:var(--white);font-weight:600;font-size:13px;display:flex;align-items:center;justify-content:center}

/* footer */
.site-footer{left:0;top:3276px;width:1200px;height:264px;background:var(--footer)}
.footer-brand{left:0;top:3368px;width:1200px;display:flex;justify-content:center;align-items:center;gap:12px;font-family:var(--display);font-weight:700;font-size:26px;color:var(--white);letter-spacing:1px}
.footer-brand .brand-mark{width:18px;height:18px}
.footer-nav{left:0;top:3428px;width:1200px;display:flex;justify-content:center;gap:24px;font-weight:500;font-size:15px;color:var(--white)}
.copyright{left:0;top:3457px;width:1200px;text-align:center;font-size:14px;color:var(--white)}
.to-top{left:1113px;top:3454px}
</style>
</head>
<body>

<header class="abs site-header">
  <div class="abs brand"><span class="brand-mark"></span>VALMIKE GROUP</div>
  <nav class="abs main-nav">
    <span class="active">HOME</span><span>ABOUT</span><span>SERVICES</span><span>IRON FINCH</span>
    <span class="nav-cta">CONTACT US</span>
  </nav>
</header>

<section class="abs hero">
  <div class="abs hero-photo" role="img" aria-label="Golden Gate Bridge at dusk with the San Francisco skyline across the bay"></div>
  <h1 class="abs hero-title hero-kicker">WELCOME TO VALMIKE GROUP</h1>
  <p class="abs hero-title hero-motto">NEW ERA IN PROTECTION</p>
  <svg class="abs hero-shape" width="1200" height="785" viewBox="0 0 1200 785">
    <polygon points="0,617 600,785 0,785" fill="#ffffff"/>
    <polygon points="1200,612 1200,785 600,785" fill="#ffffff"/>
    <polygon points="1200,612 1200,670 600,785 560,775" fill="#9b1b1e"/>
    <polygon points="205,670 600,785 600,780 215,670" fill="#9b1b1e"/>
    <g transform="translate(600,692)">
      <rect x="-19" y="-19" width="38" height="38" transform="rotate(45)" fill="none" stroke="#fff" stroke-width="2"/>
      <polyline points="-3,-6 3,0 -3,6" fill="none" stroke="#fff" stroke-width="2"/>
    </g>
  </svg>
</section>

<h2 class="abs eyebrow about-eyebrow">ABOUT</h2>
<p class="abs section-title about-title">VALMIKE GROUP</p>
<p class="abs copy about-copy">Lorem Ipsum is simply dummy text of the printing and typesetting industry. Lorem Ipsum has been the industry's standard dummy text ever since the 1500s, when an unknown printer took a galley of type and scrambled it to make a type specimen book. It has survived not only five centuries, but also the leap into electronic typesetting, remaining essentially unchanged.</p>

<div class="abs services-band"></div>
<div class="abs red-rule" style="left:272px;top:1055px;height:249px"></div>

<h2 class="abs eyebrow center-head" style="top:1329px">VALMIKE</h2>
<p class="abs section-title center-head" style="top:1356px">OUR SERVICES</p>

<article class="abs service-card" style="left:89px">
  <svg class="card-bg" width="330" height="358"><polygon points="0,0 330,0 330,282 165,358 0,282" fill="#fff"/></svg>
  <svg class="service-icon" width="100" height="95" viewBox="0 0 100 95">
    <path d="M50 4 L90 20 Q92 65 50 92 Q8 65 10 20 Z" fill="none" stroke="#111" stroke-width="3"/>
    <circle cx="36" cy="42" r="9" fill="none" stroke="#111" stroke-width="3"/>
    <circle cx="64" cy="42" r="9" fill="none" stroke="#111" stroke-width="3"/>
    <circle cx="50" cy="60" r="7" fill="none" stroke="#9b1b1e" stroke-width="3"/>
    <path d="M38 86 Q50 66 62 86" fill="none" stroke="#9b1b1e" stroke-width="3"/>
  </svg>
  <h3 class="service-name">EXECUTIVE PROTECTION</h3>
  <p class="service-copy">Lorem Ipsum is simply dummy text of the printing and typesetting industry. Lorem Ipsum has been the industry's.</p>
  <svg class="diamond-btn" viewBox="0 0 32 32"><rect x="5" y="5" width="22" height="22" transform="rotate(45 16 16)" fill="#9b1b1e"/><polyline points="14,11 19,16 14,21" fill="none" stroke="#fff" stroke-width="2"/></svg>
</article>

<article class="abs service-card" style="left:436px">
  <svg class="card-bg" width="330" height="358"><polygon points="1,1 329,1 329,282 165,357 1,282" fill="#fff" stroke="#9b1b1e" stroke-width="2"/></svg>
  <svg class="service-icon" width="100" height="95" viewBox="0 0 100 95">
    <path d="M50 4 L86 18 Q88 65 50 92 Q12 65 14 18 Z" fill="none" stroke="#111" stroke-width="3"/>
    <rect x="38" y="44" width="24" height="20" fill="none" stroke="#9b1b1e" stroke-width="3"/>
    <path d="M42 44 V36 Q50 26 58 36 V44" fill="none" stroke="#9b1b1e" stroke-width="3"/>
    <circle cx="50" cy="54" r="2.5" fill="#9b1b1e"/>
  </svg>
  <h3 class="service-name">COVERT PROTECTION</h3>
  <p class="service-copy">Lorem Ipsum is simply dummy text of the printing and typesetting industry. Lorem Ipsum has been the industry's.</p>
  <svg class="diamond-btn" viewBox="0 0 32 32"><rect x="5" y="5" width="22" height="22" transform="rotate(45 16 16)" fill="#9b1b1e"/><polyline points="14,11 19,16 14,21" fill="none" stroke="#fff" stroke-width="2"/></svg>
</article>

<article class="abs service-card" style="left:781px">
  <svg class="card-bg" width="330" height="358"><polygon points="0,0 330,0 330,282 165,358 0,282" fill="#fff"/></svg>
  <svg class="service-icon" width="100" height="95" viewBox="0 0 100 95">
    <path d="M42 4 L72 16 V40 M42 4 L12 16 Q10 62 42 88" fill="none" stroke="#111" stroke-width="3"/>
    <path d="M42 4 V88" stroke="#111" stroke-width="3"/>
    <path d="M52 62 L74 42 L96 62 M58 57 V92 H90 V57" fill="none" stroke="#9b1b1e" stroke-width="3"/>
    <rect x="68" y="72" width="12" height="20" fill="none" stroke="#9b1b1e" stroke-width="3"/>
  </svg>
  <h3 class="service-name">RESIDENTIAL PROTECTION ...</h3>
  <p class="service-copy">Lorem Ipsum is simply dummy text of the printing and typesetting industry. Lorem Ipsum has been the industry's.</p>
  <svg class="diamond-btn" viewBox="0 0 32 32"><rect x="5" y="5" width="22" height="22" transform="rotate(45 16 16)" fill="#9b1b1e"/><polyline points="14,11 19,16 14,21" fill="none" stroke="#fff" stroke-width="2"/></svg>
</article>

<div class="abs red-rule" style="left:599px;top:1790px;height:248px"></div>

<h2 class="abs eyebrow finch-eyebrow">IRON FINCH</h2>
<p class="abs section-title finch-title">TRAINING &amp;<br>CONSULTING</p>
<p class="abs copy finch-copy">Lorem Ipsum is simply dummy text of the printing and typesetting industry. Lorem Ipsum has been the industry's standard dummy text ever since the 1500s, when an unknown printer took a galley of type and scrambled it to make a type specimen book. It has survived not only five centuries, but also the leap into electronic typesetting, remaining essentially unchanged.</p>
<div class="abs read-more">READ MORE</div>
<div class="abs finch-visual" role="img" aria-label="Large brand emblem in red with a training facility photograph inside"></div>

<div class="abs contact-bg" role="img" aria-label="Faded grey city skyline over the water"></div>
<div class="abs red-rule" style="left:598px;top:2381px;height:248px"></div>

<h2 class="abs eyebrow center-head" style="top:2652px">VALMIKE</h2>
<p class="abs section-title center-head" style="top:2679px">CONTACT US</p>
<p class="abs contact-lead">To contact Valmike Group please email us or use the<br>the contact form below.</p>

<div class="abs field" style="left:333px;top:2781px;width:264px">Name</div>
<div class="abs field" style="left:604px;top:2781px;width:263px">Email</div>
<div class="abs field" style="left:333px;top:2826px;width:264px">Phone</div>
<div class="abs field" style="left:604px;top:2826px;width:263px">Subject</div>
<div class="abs field" style="left:333px;top:2868px;width:534px;height:134px">Message</div>
<div class="abs submit">SUBMIT NOW</div>

<footer class="abs site-footer"></footer>
<div class="abs footer-brand"><span class="brand-mark"></span>VALMIKE GROUP</div>
<nav class="abs footer-nav"><span>Home</span><span>About</span><span>Services</span><span>Iron Finch</span><span>Contact Us</span></nav>
<p class="abs copyright">Copyright 2021 | All Rights Reserved</p>
<svg class="abs to-top" width="44" height="44" viewBox="0 0 44 44">
  <rect x="8" y="8" width="28" height="28" transform="rotate(45 22 22)" fill="#c8232a"/>
  <polyline points="16,25 22,19 28,25" fill="none" stroke="#fff" stroke-width="2.5"/>
</svg>

</body>
</html>
```